Quorlan.com (Dedicated servers Provider)

We provide dedicated servers for clients around the world. We have created a layout for you. You need to create exactly the design based on these sketches. All text, you can take from our sketches (later we will replace them).

Target Market(s)

Web site owners and web developers

Requirements
Should not have
• The design should not use old-style fonts.

```html
<!DOCTYPE html>
<html lang="en">
<head>
<meta charset="utf-8">
<title>Quorlan.com – Dedicated Servers</title>
<link rel="stylesheet" href="https://fonts.googleapis.com/css2?family=Arimo:wght@400;700&family=Oswald:wght@300;400&display=swap">
<style>
:root{
  --page:#ffffff;
  --header-dark:#1e1e1e;
  --nav-sep:#151515;
  --green:#76b82a;
  --orange:#f39c12;
  --ink:#222222;
  --panel:#f6f6f6;
  --panel-line:#d6d6d6;
  --tab-off:#e3e3e3;
  --red:#c9221c;
  --quote-bg:#e6e6e6;
  --quote-ink:#8a8a8a;
  --partner-ink:#8f8f8f;
  --night-line:#2e2e2e;
  --night-text:#9a9a9a;
  --night-mark:#e6e6e6;
  --link:#3a9bd9;
  --pink:#c2185b;
}
*{box-sizing:border-box;margin:0;padding:0}
html,body{width:1200px;height:900px;overflow:hidden;background:var(--page)}
body{position:relative;font-family:"Arimo",Arial,sans-serif;color:var(--ink)}
.abs{position:absolute}

/* header */
.site-header{left:303px;top:0;width:594px;height:71px;background:linear-gradient(#333,#262626)}
.brand{left:79px;top:8px;display:flex;align-items:center;gap:5px}
.brand-square{width:22px;height:22px;background:var(--green)}
.brand-name{font-size:24px;font-weight:700;color:#e8e8e8;letter-spacing:-.5px;line-height:1}
.brand-sub{left:106px;top:34px;font-size:6px;color:var(--green);letter-spacing:2px}
.top-links{left:329px;top:17px;display:flex;gap:4px}
.top-link{height:12px;padding:0 6px;background:var(--header-dark);border:1px solid #3b3b3b;color:#fff;font-size:5.5px;font-weight:700;display:flex;align-items:center;gap:4px}
.top-link i{display:block;width:5px;height:6px;background:#d8b64a;border-radius:1px}
.top-link i.chat{background:#8fbf4a;width:8px;border-radius:2px}
.main-nav{left:76px;top:45px;height:25px;display:flex;background:#202020}
.main-nav a{display:flex;align-items:center;justify-content:center;height:25px;color:#fff;font-size:6px;font-weight:700;text-decoration:none;border-right:1px solid var(--nav-sep)}
.main-nav a.current{background:var(--green)}
.main-nav a.order{color:var(--orange)}

/* announcement */
.notice-bar{left:382px;top:71px;width:436px;height:16px;background:var(--green);display:flex;align-items:center;padding:0 8px;font-size:5.5px;font-weight:700;color:#fff}
.notice-icon{width:10px;height:8px;background:#dff0c8;border-radius:1px;margin-right:5px}
.notice-bar .more{color:#1d3a05;margin-left:2px}
.follow{margin-left:auto;display:flex;align-items:center;gap:3px}
.follow span{display:block;width:9px;height:9px;background:#3d8fd1;border-radius:2px}
.follow b{margin-right:2px}

/* hero */
.hero{left:382px;top:95px;width:436px;height:142px;background:#1a1a1a;overflow:hidden}
.hero-left{left:0;top:0;width:253px;height:118px;background:linear-gradient(90deg,#1d1d1d,#2e2e2e 40%,#3c3c3c)}
.hero-title{left:29px;top:5px;font-family:"Oswald",Arial,sans-serif;font-weight:300;font-size:21px;line-height:26px;color:#fff;letter-spacing:1.2px;white-space:nowrap}
.hero-from{left:29px;top:27px;width:202px;text-align:right;font-size:4px;color:#bbb;font-weight:700;font-style:normal;letter-spacing:.3px}
.hero-server{left:28px;top:38px;width:82px;height:74px;background:radial-gradient(ellipse at 45% 40%,#5a5a5a,#2a2a2a 55%,#151515 80%,#2e2e2e)}
.hero-points{left:133px;top:42px;list-style:none;color:#fff;font-size:6px;font-weight:700;line-height:10px}
.hero-points li::before{content:"";display:inline-block;width:3px;height:3px;background:#888;border-radius:50%;margin-right:5px;vertical-align:middle}
.hero-btn{left:140px;top:96px;width:44px;height:12px;background:var(--green);color:#fff;font-size:5px;display:flex;align-items:center;justify-content:center}
.hero-photo{left:253px;top:0;width:183px;height:118px;background:linear-gradient(90deg,#2c2c2c 0,#3a3a3a 35%,#6b5a4e 62%,#5a1e22 80%,#2a2a2a)}
.hero-script{left:258px;top:36px;width:116px;font-family:"Oswald",Arial,sans-serif;font-weight:300;font-size:7.5px;line-height:9.5px;color:#e6e6e6;letter-spacing:.5px}
.hero-strip{left:0;top:118px;width:436px;height:24px;background:#0c0c0c}
.hiring-icon{left:8px;top:4px}
.hiring{left:34px;top:3px;color:#fff;font-size:9px}
.hiring-tag{left:34px;top:14px;background:var(--pink);color:#fff;font-size:4.5px;padding:1px 2px}
.call{right:8px;top:7px;color:#fff;font-size:9px;font-weight:700}
.call span{font-weight:400}

/* tabs */
.tab{top:247px;width:105px;height:18px;font-size:6.5px;font-weight:700;color:#999;display:flex;align-items:center;justify-content:center;background:var(--tab-off);border:1px solid var(--panel-line);border-bottom:none}
.tab.active{background:#fff;color:#444;height:19px;z-index:2}

/* plans */
.plans{left:382px;top:264px;width:420px;height:117px;background:var(--panel);border:1px solid var(--panel-line);display:flex}
.plan{position:relative;width:137px;height:100%;border-right:1px solid var(--panel-line)}
.plan:last-child{border-right:none}
.plan-name{position:absolute;left:0;right:0;top:7px;text-align:center;font-size:9.5px;font-weight:700;color:#222}
.plan-image{position:absolute;left:27px;top:27px;width:78px;height:28px;background:linear-gradient(90deg,#6fae3f 0 20px,#8a8a8a 20px,#3a3a3a)}
.plan-from{position:absolute;left:27px;top:60px;font-size:4px;font-weight:700}
.plan-price{position:absolute;left:12px;top:64px;font-size:21px;font-weight:700;line-height:1;letter-spacing:-.5px;display:flex}
.plan-price sup{font-size:9px;line-height:1;margin-top:2px;text-decoration:underline}
.plan-per{position:absolute;left:48px;top:80px;font-size:3.5px}
.plan-specs{position:absolute;left:69px;top:58px;font-size:5px;line-height:8px;color:#333;list-style:none}
.plan-select{position:absolute;left:69px;top:84px;width:62px;height:8px;border:1px solid #aaa;background:#fff;font-size:4px;padding-left:2px;line-height:6px}
.plan-link{position:absolute;left:17px;top:102px;font-size:5px;text-decoration:underline;color:#333}
.plan-order{position:absolute;left:79px;top:97px;width:40px;height:12px;background:var(--red);color:#fff;font-size:6.5px;font-weight:700;display:flex;align-items:center;justify-content:center;border-radius:2px}

/* assurances */
.assurances{left:382px;top:380px;width:420px;height:72px;background:#ececec;border:1px solid var(--panel-line);border-top:none}
.network-map{left:13px;top:5px;width:88px;height:55px;background:radial-gradient(ellipse at 50% 55%,#8ec3de,#5a9dc2 60%,#ececec 72%)}
.map-caption{left:18px;top:63px;font-size:4px;color:#555}
.assure{font-size:6.5px;font-weight:700;display:flex;align-items:center;gap:5px}
.tick{width:11px;height:11px}

/* testimonial */
.testimonial{left:382px;top:458px;width:420px;height:107px;background:var(--quote-bg);border-top:2px solid #bbb}
.quote-mark{font-family:"Oswald",Arial,sans-serif;font-size:48px;color:#b9b9b9;line-height:1}
.quote-text{left:48px;top:16px;width:316px;text-align:center;font-family:"Oswald",Arial,sans-serif;font-weight:300;font-size:10.5px;line-height:10.5px;letter-spacing:.4px;color:var(--quote-ink);text-transform:uppercase}
.quote-author{left:0;width:420px;top:76px;text-align:center;font-size:6.5px;color:#666}

/* partners */
.partners{left:386px;top:573px;width:386px;height:22px;display:flex;justify-content:space-between;align-items:center}
.partner-name{font-size:8px;font-weight:700;color:var(--partner-ink);letter-spacing:-.2px}
.partner-badge{height:14px;background:#c4c4c4;border-radius:2px}

/* info block */
.info{left:382px;top:603px;width:420px;height:292px;background:linear-gradient(#1c1c1c,#111)}
.info-title{left:18px;top:18px;font-size:7.5px;color:#fff}
.perk{width:125px}
.perk-icon{position:absolute;left:0;top:1px;width:16px;height:15px;background:#555;border-radius:3px}
.perk h3{position:absolute;left:26px;top:0;font-size:5.5px;color:#fff}
.perk p{position:absolute;left:26px;top:9px;width:100px;font-size:4.3px;line-height:5.6px;color:var(--night-text)}
.stat-dot{position:absolute;left:0;top:3px;width:4px;height:4px;border-radius:50%;background:#888}
.stat-num{position:absolute;left:9px;top:0;font-size:12px;font-weight:700;color:#fff;line-height:1}
.stat-text{position:absolute;left:9px;top:13px;width:54px;font-size:4.3px;line-height:5.6px;color:var(--night-text)}
.rule{height:1px;background:var(--night-line)}
.vrule{width:1px;background:var(--night-line)}
.col-title{font-size:5.5px;color:#fff;font-weight:700}
.keep-title{font-size:10px;color:#fff;font-weight:700}
.keep-text{font-size:6px;line-height:7px;color:var(--night-text);width:125px}
.link{color:var(--link)}
.small{font-size:4.3px;line-height:6px;color:var(--night-text)}
.phone{font-size:10px;color:#fff;font-weight:700}
.social-btn{height:8px;border-radius:2px;font-size:4.5px;color:#fff;display:flex;align-items:center;padding:0 3px}
.footer-name{font-size:7.5px;font-weight:700;color:var(--night-mark);line-height:1}
.footer-dot{width:14px;height:14px;border-radius:50%;background:#4a4a4a}
.award{font-size:5px;font-weight:700;color:#fff;line-height:5.5px;text-align:right}
.award span{color:var(--link);font-weight:400}
.award-seal{width:22px;height:22px;border-radius:50%;background:#444}
.sitemap{width:40px;height:11px;background:#2c4a6a;color:#fff;font-size:4.5px;display:flex;align-items:center;justify-content:center}
</style>
</head>
<body>

<header class="site-header abs">
  <div class="brand abs"><span class="brand-square"></span><span class="brand-name">Quorlan</span></div>
  <div class="brand-sub abs">servers</div>
  <div class="top-links abs">
    <span class="top-link">User Registration <i></i></span>
    <span class="top-link">Customer Login <i></i></span>
    <span class="top-link">Live Chat Online <i class="chat"></i></span>
  </div>
  <nav class="main-nav abs">
    <a class="current" style="width:42px">HOME</a>
    <a style="width:63px">DOMAINS</a>
    <a style="width:70px">WEBHOSTING</a>
    <a style="width:68px">LATEST NEWS</a>
    <a style="width:72px">MY ACCOUNT</a>
    <a style="width:70px">CONTACT US</a>
    <a class="order" style="width:58px;border-right:none">ORDERNOW</a>
  </nav>
</header>

<div class="notice-bar abs">
  <span class="notice-icon"></span>
  Got an important announcement or a special offer? Tell your customer about it! <span class="more">Read More</span>
  <div class="follow"><b>Follow Us:</b><span></span><span></span><span></span></div>
</div>

<section class="hero abs">
  <div class="hero-left abs"></div>
  <div class="hero-title abs">DEDICATED SERVERS</div>
  <div class="hero-from abs">FROM FASTRACK</div>
  <div class="hero-server abs" role="img" aria-label="Rack of blade servers"></div>
  <ul class="hero-points abs">
    <li>Self-owned data centre</li>
    <li>24 x 7 x 365 on-site support</li>
    <li>100% uptime guarantee</li>
    <li>Industry leading control panel</li>
    <li>Custom servers; 24 hour setup</li>
  </ul>
  <div class="hero-btn abs">Find out more</div>
  <div class="hero-photo abs" role="img" aria-label="Photo of a smiling businessman in a dark suit and red shirt"></div>
  <p class="hero-script abs">Sed consequat ornare quam. Vivamus pulvinar sollicitudin. Vivamus id risus sed pede convallis fringilla.</p>
  <div class="hero-strip abs">
    <svg class="hiring-icon abs" width="18" height="17" viewBox="0 0 18 17"><circle cx="9" cy="5" r="4" fill="#fff"/><path d="M1 17c0-5 4-7 8-7s8 2 8 7z" fill="#fff"/></svg>
    <div class="hiring abs">We Are Hiring</div>
    <div class="hiring-tag abs">Apply online Now</div>
    <div class="call abs">Call us Today <span>123456-789</span></div>
  </div>
</section>

<div class="tab active abs" style="left:382px">Dedicated Servers</div>
<div class="tab abs" style="left:495px">Web Hosting</div>
<div class="tab abs" style="left:608px">Virtual Private Servers</div>

<section class="plans abs">
  <div class="plan">
    <div class="plan-name">Corvex 4 2.4GHz</div>
    <div class="plan-image" role="img" aria-label="Server unit"></div>
    <div class="plan-from">Plans starting at</div>
    <div class="plan-price">$39<sup>00</sup></div>
    <div class="plan-per">per mo</div>
    <ul class="plan-specs"><li>80GB SATA HD</li><li>1GB RAM</li><li>1TB Bandwidth</li></ul>
    <div class="plan-select">1 year – 39.00/mo</div>
    <div class="plan-link">All Dedicated Servers</div>
    <div class="plan-order">ORDER</div>
  </div>
  <div class="plan">
    <div class="plan-name">Corvex 7 2.66-2.93Ghz</div>
    <div class="plan-image" role="img" aria-label="Server unit"></div>
    <div class="plan-from">Plans starting at</div>
    <div class="plan-price">$219<sup>00</sup></div>
    <div class="plan-per" style="left:62px">per mo</div>
    <ul class="plan-specs"><li>500 SATA HD</li><li>6GB RAM</li><li>8TB Bandwidth</li></ul>
    <div class="plan-select">1 year – 219.00/mo</div>
    <div class="plan-link">All Dedicated Servers</div>
    <div class="plan-order">ORDER</div>
  </div>
  <div class="plan">
    <div class="plan-name">Dual Argon E5-2620</div>
    <div class="plan-image" role="img" aria-label="Server unit"></div>
    <div class="plan-from">Plans starting at</div>
    <div class="plan-price">$395<sup>00</sup></div>
    <div class="plan-per" style="left:62px">per mo</div>
    <ul class="plan-specs"><li>1000 SATA HD</li><li>16GB RAM</li><li>10TB Bandwidth</li></ul>
    <div class="plan-select">1 year – 395.00/mo</div>
    <div class="plan-link">All Dedicated Servers</div>
    <div class="plan-order">ORDER</div>
  </div>
</section>

<section class="assurances abs">
  <div class="network-map abs" role="img" aria-label="Map of the United States with network routes"></div>
  <div class="map-caption abs">Now offering Nimbus Control Panel 11</div>
  <div class="assure abs" style="left:122px;top:12px"><svg class="tick" viewBox="0 0 12 12"><circle cx="6" cy="6" r="6" fill="#c9221c"/><path d="M3 6.2l2 2 4-4.4" stroke="#fff" stroke-width="1.6" fill="none"/></svg>100% Network Uptime SLA</div>
  <div class="assure abs" style="left:122px;top:30px"><svg class="tick" viewBox="0 0 12 12"><circle cx="6" cy="6" r="6" fill="#c9221c"/><path d="M3 6.2l2 2 4-4.4" stroke="#fff" stroke-width="1.6" fill="none"/></svg>ISO 9001:2008 Certified</div>
  <div class="assure abs" style="left:122px;top:49px"><svg class="tick" viewBox="0 0 12 12"><circle cx="6" cy="6" r="6" fill="#c9221c"/><path d="M3 6.2l2 2 4-4.4" stroke="#fff" stroke-width="1.6" fill="none"/></svg>24/7 ITIL Technical Support</div>
  <div class="assure abs" style="left:254px;top:12px"><svg class="tick" viewBox="0 0 12 12"><circle cx="6" cy="6" r="6" fill="#c9221c"/><path d="M3 6.2l2 2 4-4.4" stroke="#fff" stroke-width="1.6" fill="none"/></svg>3 SSAE-16 Certified Data Centers</div>
  <div class="assure abs" style="left:254px;top:30px"><svg class="tick" viewBox="0 0 12 12"><circle cx="6" cy="6" r="6" fill="#c9221c"/><path d="M3 6.2l2 2 4-4.4" stroke="#fff" stroke-width="1.6" fill="none"/></svg>Coast-to-Coast IP Backbone</div>
  <div class="assure abs" style="left:254px;top:49px"><svg class="tick" viewBox="0 0 12 12"><circle cx="6" cy="6" r="6" fill="#c9221c"/><path d="M3 6.2l2 2 4-4.4" stroke="#fff" stroke-width="1.6" fill="none"/></svg>Award Winning Since 1996</div>
</section>

<section class="testimonial abs">
  <div class="quote-mark abs" style="left:16px;top:12px">“</div>
  <div class="quote-mark abs" style="left:366px;top:26px">”</div>
  <p class="quote-text abs">We had been badly let down by several companies over the last few years, but last year I found hostmeadow.com on search &amp; within 15 minutes I had received a response back from Martin with full pricing &amp; my server is still running perfectly, with no downtime</p>
  <div class="quote-author abs">Sam Orwell orwellnet.com</div>
</section>

<div class="partners abs">
  <span class="partner-name">Intello</span>
  <span class="partner-badge" style="width:12px;height:18px"></span>
  <span class="partner-name">DataSQL</span>
  <span class="partner-badge" style="width:32px;height:12px"></span>
  <span class="partner-badge" style="width:30px;height:14px"></span>
  <span class="partner-badge" style="width:20px;height:18px;border-radius:50%"></span>
  <span class="partner-name">Corepanel</span>
  <span class="partner-name">Parallax</span>
  <span class="partner-name">Netrik</span>
</div>

<section class="info abs">
  <h2 class="info-title abs" style="font-weight:400">ClearServers - The Smart Choice For Dedicated Servers</h2>

  <div class="perk abs" style="left:18px;top:38px"><span class="perk-icon"></span><h3>Business-Class ProBuild Hardware</h3><p>We use high-end ProBuild hardware, robust and reliable for building your ideal server.</p></div>
  <div class="perk abs" style="left:148px;top:38px"><span class="perk-icon"></span><h3>99.9% Uptime SLA</h3><p>A fully redundant network and infrastructure backed up by our 99.9% Uptime Guarantee.</p></div>
  <div class="perk abs" style="left:278px;top:38px"><span class="perk-icon"></span><h3>24/7/365 Expert UK Technical Support</h3><p>Our expert NOC technicians are available by phone and email support all day, every day.</p></div>
  <div class="perk abs" style="left:18px;top:76px"><span class="perk-icon"></span><h3>Fast Setup</h3><p>Guaranteed instant setup of pre-configured servers and within 24 hours for customised.</p></div>
  <div class="perk abs" style="left:148px;top:76px"><span class="perk-icon"></span><h3>Dedicated Account Manager</h3><p>No long call queues, machines or being passed around, just one point of contact.</p></div>
  <div class="perk abs" style="left:278px;top:76px"><span class="perk-icon"></span><h3>Simple Customisation</h3><p>Customising your server online is quick and simple, plus you can upgrade at any time.</p></div>

  <h2 class="info-title abs" style="top:120px">ClearServers is part of the Norvia Group - check out our stats!</h2>

  <div class="abs" style="left:18px;top:135px;width:90px;height:30px"><span class="stat-dot"></span><span class="stat-num">1,800,000</span><span class="stat-text">domains registered in over 250 extensions</span></div>
  <div class="abs" style="left:113px;top:135px;width:90px;height:30px"><span class="stat-dot"></span><span class="stat-num">40,000</span><span class="stat-text">new registrations per month</span></div>
  <div class="abs" style="left:210px;top:135px;width:90px;height:30px"><span class="stat-dot"></span><span class="stat-num">500,000</span><span class="stat-text">websites hosted on our platform</span></div>
  <div class="abs" style="left:306px;top:135px;width:90px;height:30px"><span class="stat-dot"></span><span class="stat-num">490,000</span><span class="stat-text">clients are using our products</span></div>

  <div class="rule abs" style="left:0;top:168px;width:420px"></div>
  <div class="vrule abs" style="left:146px;top:176px;height:72px"></div>
  <div class="vrule abs" style="left:280px;top:176px;height:72px"></div>

  <div class="keep-title abs" style="left:18px;top:181px">Keep it simple!</div>
  <p class="keep-text abs" style="left:18px;top:199px">The web changes people and the things they do. This is why we develop increasingly reliable, easy-to-use and intuitive services.</p>
  <div class="abs link" style="left:18px;top:237px;font-size:5.5px;font-weight:700">Learn more about ClearServers</div>

  <div class="col-title abs" style="left:152px;top:180px">About ClearServers</div>
  <div class="small abs" style="left:152px;top:192px"><span class="link">About Us</span><br><span class="link">Contact Us</span><br><span class="link">Terms &amp; Conditions</span></div>
  <div class="small abs" style="left:208px;top:192px"><span class="link">Support</span><br><span class="link">Why Choose Us</span><br><span class="link">Service Level Agreement</span></div>
  <div class="small abs" style="left:152px;top:226px">Copyright © Kelbrook Ltd 2012. All rights reserved</div>
  <div class="small abs" style="left:152px;top:237px;width:124px">ClearServers is part of the <span class="link">Norvia Group</span>. Read more on the Norvia <span class="link">Blog</span></div>

  <div class="col-title abs" style="left:286px;top:180px">Information</div>
  <div class="small abs" style="left:286px;top:194px;width:125px">Contact us via our Support Ticket System in your <span class="link">Online Control Panel</span> or alternatively call us on the number below:</div>
  <div class="phone abs" style="left:286px;top:213px">+44 (0)1000 555 010</div>
  <div class="social-btn abs" style="left:286px;top:232px;background:#4a66a0">Like 12</div>
  <div class="social-btn abs" style="left:326px;top:232px;background:#2a7fb8">Follow @clearservers</div>
  <div class="small abs" style="left:286px;top:244px">+1 &nbsp; Recommend this page</div>

  <div class="rule abs" style="left:0;top:257px;width:420px"></div>
  <div class="footer-name abs" style="left:18px;top:273px">ProBuild</div>
  <div class="footer-name abs" style="left:56px;top:273px">Maxsoft</div>
  <div class="footer-name abs" style="left:92px;top:273px">Plexon</div>
  <div class="footer-name abs" style="left:124px;top:273px">Verity</div>
  <div class="footer-dot abs" style="left:156px;top:270px"></div>
  <div class="footer-name abs" style="left:176px;top:273px">Parallax</div>
  <div class="footer-name abs" style="left:214px;top:273px">Intello</div>
  <div class="award abs" style="left:262px;top:268px">AWARD WINNING<br>DEDICATED HOSTING<br><span>View Our Awards</span></div>
  <div class="award-seal abs" style="left:327px;top:266px"></div>
  <div class="sitemap abs" style="left:368px;top:271px">Show Site Map</div>
</section>

</body>
</html>
```